Corporate Design für Kommunikations- und Verwaltungsnetzwerk
TUVEK is a very attentive and fast designer. The communication was delightful and professional. Despite his top ranking on this plattform, he is genuine, humble and just like the trusty designer in your neighbourhood.
Zielgruppe
tosali ist 5 Monate altes Startup. Wir entwickeln ein neues Kommunikations- und Verwaltungsnetzwerk für die unten genannte Zielgruppe. Dazu bauen wir eine Web-Plattform, sowie eine App. Das Produkt als solches ist daher kein physisches sondern besitzt reinen Service-Charakter.
Zielgruppe:
Die Zielkunden von tosali bestehen aus Gruppen von Menschen, die sich freiwillig, ehrenamtlich oder auch hauptberuflich einer gemeinsamen Aufgabe widmen und dabei komplexe Anforderungen bezüglich Verwaltung und Organisation der Mitglieder, des technischen Vereinsequipments, der Kommunikation oder der Umsetzung rechtlich verbindlicher Prozesse haben. Diese Voraussetzungen finden sich in Fliegervereinen, vor allem aber bei Behörden und Organisationen mit Sicherheitsaufgaben (BOS), wie z.B. Feuerwehren. Auch mit im Boot sitzen die jeweiligen Verbände.
The startup `tosali` is 5 months young. We are developing a new communication and managment network for the target audience mentioned below. We are building a web platform as well as an app. The product isn't a physical one but is merely an IT-Service.
Target Audience:
The target audience of tosali consists of groups of people, which follow a common cause by their own free will, voluntarily or full-time. The accomplischment of the goals involved usually has got complex requirements regarding the management and organization of persons, regarding the technical equipment, the communication or the handling of legal processes.
These requirements can be found in flight clubs, but mostly in agencies and organizations located in the security sector, e.g. fire departments. Also part of the target audience are the associations affiliated.
Aufgabenstellung
tosali setzt sich aus den 3 englischen Wörter me, we und do zusammen. Dahinter steckt die einfache Botschaft, dass die Einzelperson mit anderen Personen zusammen etwas tut - ein typischer Ablauf in Vereinen. Der Fokus liegt auf der Gemeinschaft und der Vernetzung.
Hinweise zum Design:
- Die Schriftart sollte einen modernen, technischen oder sci-fi Charakter haben.
- Farblich muss es nicht bei den 3 Farben bleiben, weniger Farben sind auch denkbar.
- Wichtig bleibt eine farbliche oder anders geartete sichtbare Trennung der 3 Wörter me, we, do
tosali is made up of the 3 english words me, we and do.
The simple message behind this is: A single person does something together with other people.
This is a process you typically find in clubs. The focus is on the community and networking.
Tips for the design:
- The typeface should be modern, technical or sci-fi
- The design could use less than the 3 colors of our current logo. Sometimes less is more.
- It is important to us to have the 3 words me, we, do visually separated. This can be done using different colors or other means of your liking.

```html
<!DOCTYPE html>
<html lang="de">
<head>
<meta charset="utf-8">
<title>tosali – Geschäftsausstattung</title>
<link rel="stylesheet" href="https://fonts.googleapis.com/css2?family=Nunito+Sans:wght@400;600&family=Arimo:wght@400&display=swap">
<style>
:root{
  --board:#96979b;
  --paper:#ffffff;
  --paper-soft:#f7f8fa;
  --ink:#0b0c0e;
  --night:#07080a;
  --green:#7cc242;
  --body-grey:#6f7073;
  --window:#d0d0d0;
  --line:#a9abaf;
}
*{margin:0;padding:0;box-sizing:border-box}
html,body{width:1200px;height:1200px;overflow:hidden;background:var(--paper)}
.board{position:absolute;left:111px;top:0;width:977px;height:1200px;background:var(--board)}
.item{position:absolute;background:var(--paper);box-shadow:0 6px 8px rgba(0,0,0,.25)}
.brand{font-family:"Nunito Sans",sans-serif;font-weight:600;color:var(--ink);letter-spacing:.08em;line-height:1;position:absolute;white-space:nowrap;display:flex;align-items:center;gap:.25em}
.brand .dot{width:.35em;height:.35em;border-radius:50%;background:var(--green);display:inline-block}
.tagline{font-family:"Nunito Sans",sans-serif;font-weight:400;line-height:1;position:absolute;white-space:nowrap;color:var(--ink)}
.text{font-family:Arimo,sans-serif;color:var(--body-grey);position:absolute}

/* logo sheet */
.logo-sheet{left:341px;top:42px;width:335px;height:492px;box-shadow:none}
.logo-sheet .light{position:absolute;left:0;top:0;width:100%;height:246px;background:var(--paper)}
.logo-sheet .dark{position:absolute;left:0;top:246px;width:100%;height:246px;background:var(--night)}
.logo-sheet .brand{font-size:36px;left:36px;top:100px}
.logo-sheet .tagline{font-size:16px;left:80px;top:140px}
.logo-sheet .dark .brand{color:var(--paper);top:106px}
.logo-sheet .dark .tagline{color:var(--paper);top:146px}

/* business cards */
.card-front{left:728px;top:184px;width:161px;height:104px}
.card-front .brand{font-size:17px;left:22px;top:40px}
.card-front .tagline{font-size:6.5px;left:42px;top:61px}
.card-back{left:725px;top:309px;width:161px;height:105px}
.card-back .brand{font-size:11px;left:8px;top:15px}
.card-back .tagline{font-size:4px;left:20px;top:28px;font-weight:600}
.card-back .name{font-size:7px;left:8px;top:44px;color:#555}
.card-back .role{font-size:3.6px;left:9px;top:53px;color:var(--green)}
.card-back .contact{font-size:3.6px;left:14px;top:67px;line-height:5.3px;color:#444}
.card-back .icons{position:absolute;left:9px;top:68px}

/* letter */
.letter{left:167px;top:584px;width:398px;height:563px}
.letter .brand{font-size:18px;right:22px;top:48px}
.letter .sender{font-size:4.3px;left:41px;top:87px;color:#444}
.letter .recipient{font-size:6.2px;left:41px;top:102px;line-height:8.4px}
.letter .body{font-size:6.1px;left:41px;top:183px;width:320px;line-height:8px}
.letter .body p{margin-bottom:8px}
.letter .signature{position:absolute;left:177px;top:418px;width:85px;height:44px;background:linear-gradient(90deg,rgba(0,0,0,0),rgba(0,0,0,.06),rgba(0,0,0,0))}
.letter .footer{font-size:4.3px;top:530px;line-height:6px;color:#444}

/* envelopes */
.env-front{left:617px;top:599px;width:417px;height:209px;background:var(--paper-soft)}
.env-front .brand{font-size:18px;left:39px;top:34px}
.env-front .window{position:absolute;left:39px;top:92px;width:190px;height:83px;border-radius:5px;background:var(--window)}
.env-back{left:615px;top:871px;width:417px;height:209px;background:var(--paper-soft)}
.env-back svg{position:absolute;left:0;top:0}
.env-back .brand{font-size:13px;left:182px;top:32px}
.env-back .url{font-size:7px;letter-spacing:.2em;left:172px;top:192px;color:#555}
</style>
</head>
<body>
<div class="board"></div>

<section class="item logo-sheet">
  <div class="light">
    <div class="brand">tosali<span class="dot"></span></div>
    <div class="tagline">Future Department here</div>
  </div>
  <div class="dark">
    <div class="brand">tosali<span class="dot"></span></div>
    <div class="tagline">Future Department here</div>
  </div>
</section>

<section class="item card-front">
  <div class="brand">tosali<span class="dot"></span></div>
  <div class="tagline">Future Department here</div>
</section>

<section class="item card-back">
  <div class="brand">tosali<span class="dot"></span></div>
  <div class="tagline">Future Department here</div>
  <div class="text name">Lena Vorbild</div>
  <div class="text role">Geschäftsführerin</div>
  <svg class="icons" width="4" height="30" viewBox="0 0 4 30">
    <circle cx="2" cy="1.5" r="1.2" fill="none" stroke="#7cc242" stroke-width=".6"/>
    <rect x=".6" y="13" width="2.8" height="2.2" fill="#7cc242"/>
    <rect x=".4" y="18.5" width="3.2" height="2" fill="#7cc242"/>
    <circle cx="2" cy="23.5" r="1.3" fill="none" stroke="#7cc242" stroke-width=".6"/>
  </svg>
  <div class="text contact">Lindenstraße 1<br>DE-000000 Germany<br><br>00000 000<br>info@tosali.de<br>www.tosali.de</div>
</section>

<section class="item letter">
  <div class="brand">tosali<span class="dot"></span></div>
  <div class="text sender">tosali | Lindenstraße 1 | DE- 0000 Germany</div>
  <div class="text recipient">Recipient Name<br>Organization Name<br>Street Address<br>City - Zip Code</div>
  <div class="text body">
    <p>Sehr geehrte Damen und Herren,</p>
    <p>Lorem ipsum dolor sit amet, consectetur adipisici elit, sed eiusmod tempor incidunt ut labore et dolore magna aliqua. Ut enim ad minim veniam, quis nostrud exercitation ullamco laboris nisi ut aliquid ex ea commodi consequat. Quis aute iure reprehenderit in voluptate velit esse cillum dolore eu fugiat nulla pariatur. Excepteur sint obcaecat cupiditat non proident, sunt in culpa qui officia deserunt mollit anim id est laborum</p>
    <p>Lorem ipsum dolor sit amet, consectetur adipisici elit,</p>
    <p>sed eiusmod tempor incidunt ut labore et dolore magna aliqua. Ut enim ad minim veniam, quis nostrud exercitation ullamco laboris nisi ut aliquid ex ea commodi consequat. Quis aute iure reprehenderit in voluptate velit esse cillum dolore eu fugiat nulla pariatur. Excepteur sint obcaecat cupiditat non proident, sunt in culpa qui officia deserunt mollit anim id est laborum..<br>Lorem ipsum dolor sit amet, consectetur adipisici elit, sed eiusmod tempor incidunt ut labore et dolore magna aliqua. Ut enim ad minim veniam, quis nostrud exercitation ullamco laboris nisi ut aliquid ex ea commodi consequat. Quis aute iure reprehenderit in voluptate velit esse cillum dolore eu fugiat nulla pariatur. Excepteur sint obcaecat cupiditat non proident, sunt in culpa qui officia deserunt mollit anim id est laborum.</p>
    <p style="margin-top:14px">sed eiusmod tempor incidunt ut labore et dolore magna aliqua. Ut enim ad minim veniam, quis nostrud exercitation ullamco laboris nisi ut aliquid ex ea commodi consequat. Quis aute iure reprehenderit in voluptate velit esse cillum dolore eu fugiat nulla pariatur. Excepteur sint obcaecat cupiditat non proident, sunt in culpa qui officia deserunt mollit anim id est laborum..<br>Lorem ipsum dolor sit amet, consectetur adipisici elit, sed eiusmod tempor incidunt ut labore et dolore magna aliqua. Ut enim ad minim veniam, quis nostrud exercitation ullamco laboris nisi ut aliquid ex ea commodi consequat. Quis aute iure reprehenderit in voluptate velit esse cillum dolore eu fugiat nulla pariatur. Excepteur sint obcaecat cupiditat non proident, sunt in culpa qui officia deserunt mollit anim id est laborum.</p>
    <p>Mit freundlichen Grüßen</p>
  </div>
  <div class="signature" role="img" aria-label="Handschriftliche Unterschrift"></div>
  <div class="text footer" style="left:52px"><b>tosali</b><br>Lindenstraße 1<br>DE- 0000 Germany</div>
  <div class="text footer" style="left:141px">Tel.&nbsp;&nbsp;&nbsp;0000 000<br>Fax&nbsp;&nbsp;&nbsp;0000 000<br>info@tosali.de<br>www.tosali.de</div>
  <div class="text footer" style="left:226px">Bankverbindung<br>IBAN<br>BIC<br>Ust-Ident-Nr.</div>
  <div class="text footer" style="left:271px">Beispiel Bank<br>DE00 0000 0000 0000 0000 00<br>XXXXXXXXXXX<br>DE 000000000000</div>
</section>

<section class="item env-front">
  <div class="brand">tosali<span class="dot"></span></div>
  <div class="window"></div>
</section>

<section class="item env-back">
  <svg width="417" height="209" viewBox="0 0 417 209">
    <path d="M1 0 L11 62 Q13 71 22 71 L395 71 Q404 71 406 62 L416 0" fill="none" stroke="var(--line)" stroke-width="1"/>
  </svg>
  <div class="brand">tosali<span class="dot"></span></div>
  <div class="text url">www.tosali.de</div>
</section>
</body>
</html>
```